Updated Business Card Design more modern and eye catching

looking for something more dynamic than the sterile card we have now. Please take a look at our web site www.quarvinstores.net to see what we do. only looking for the front side of the card for now. I've also attached a sample of a card with raised spot uv ink - it might be cool to incorporate something like that. Card should be bold yet serious. No frilly or scrolly stuff on it.
Updates
Target Market(s)
We do decor and signage for retail business and supermarkets. Our new name should reflect that we're hip but serious.
Contact Information for Business Card
standard business card size - horizontal preferred
Font styles to use
Requirements
Must have
- Current logo and colors cannot be changed.
Nice to have
- Must have information shown on existing card but open to some changes. Okay to consider spot uv.
Should not have
- Not busy with pictures in the background.

```html
<!DOCTYPE html>
<html lang="en">
<head>
<meta charset="utf-8">
<title>Quarvin Stores – Business Card</title>
<link href="https://fonts.googleapis.com/css2?family=Roboto:wght@400;500;700&display=swap" rel="stylesheet">
<style>
  :root{
    --gold:#b5a852;
    --ink:#111111;
    --paper:#ffffff;
    --backdrop:#2d2d2d;
    --muted:#222222;
  }
  html,body{margin:0;padding:0;overflow:hidden;}
  body{width:1200px;height:900px;background:var(--backdrop);position:relative;font-family:"Roboto",sans-serif;}
  .card{position:absolute;width:600px;height:340px;border-radius:22px;background:var(--paper);overflow:hidden;box-shadow:0 10px 30px rgba(0,0,0,.45);}
  .card-front{left:80px;top:90px;}
  .card-back{left:520px;top:480px;}

  .wordmark{display:flex;align-items:center;gap:14px;white-space:nowrap;}
  .wordmark-square{width:26px;height:26px;background:var(--gold);flex:none;}
  .wordmark-name{font-weight:500;color:var(--gold);letter-spacing:5px;text-transform:uppercase;}
  .rule{height:2px;background:var(--gold);}

  .card-front .wordmark{position:absolute;left:120px;top:132px;}
  .card-front .wordmark-name{font-size:34px;}
  .card-front .rule{position:absolute;left:160px;top:190px;width:320px;}
  .card-front .site{position:absolute;right:50px;bottom:34px;font-size:15px;color:var(--muted);}

  .card-back svg.shapes{position:absolute;left:0;top:0;}
  .card-back .wordmark{position:absolute;left:34px;top:70px;gap:10px;}
  .card-back .wordmark-square{width:16px;height:16px;}
  .card-back .wordmark-name{font-size:17px;letter-spacing:1.5px;}
  .card-back .rule{position:absolute;left:34px;top:104px;width:196px;}

  .name-band{position:absolute;left:290px;top:44px;width:180px;color:var(--paper);text-align:center;}
  .name-band .person{font-size:19px;font-weight:700;}
  .name-band .role{font-size:11px;margin-top:3px;}

  .contacts{position:absolute;left:34px;top:196px;list-style:none;margin:0;padding:0;}
  .contacts li{display:flex;align-items:center;gap:12px;height:28px;font-size:15px;color:var(--muted);}
  .contact-icon{width:22px;height:22px;background:var(--gold);display:flex;align-items:center;justify-content:center;}

  .address{position:absolute;right:40px;top:220px;width:200px;text-align:center;color:var(--paper);font-size:14px;line-height:1.35;}
  .address svg{display:block;margin:0 auto 8px;}
</style>
</head>
<body>

<section class="card card-front">
  <div class="wordmark">
    <span class="wordmark-square"></span>
    <span class="wordmark-name">Quarvin Stores</span>
  </div>
  <div class="rule"></div>
  <div class="site">www.quarvinstores.net</div>
</section>

<section class="card card-back">
  <svg class="shapes" width="600" height="340" viewBox="0 0 600 340">
    <polygon points="262,0 600,0 600,340 360,340 300,120 300,96 262,0" fill="var(--gold)"/>
    <polygon points="268,40 480,40 480,96 268,96" fill="var(--ink)"/>
    <polygon points="268,96 300,96 300,122" fill="var(--ink)"/>
  </svg>

  <div class="wordmark">
    <span class="wordmark-square"></span>
    <span class="wordmark-name">Quarvin Stores</span>
  </div>
  <div class="rule"></div>

  <div class="name-band">
    <div class="person">Dana Mercer</div>
    <div class="role">Vice - President</div>
  </div>

  <ul class="contacts">
    <li><span class="contact-icon"><svg width="12" height="12" viewBox="0 0 12 12"><path d="M2 1h3l1 3-2 1a7 7 0 0 0 3 3l1-2 3 1v3c-6 0-9-3-9-9z" fill="#fff"/></svg></span>555-310-4172</li>
    <li><span class="contact-icon"><svg width="12" height="12" viewBox="0 0 12 12"><rect x="1" y="4" width="10" height="7" rx="1" fill="none" stroke="#fff"/><path d="M1 4c2-3 8-3 10 0" fill="none" stroke="#fff"/><circle cx="6" cy="7.5" r="1.5" fill="#fff"/></svg></span>555-268-1940 ex.3</li>
    <li><span class="contact-icon"><svg width="12" height="10" viewBox="0 0 12 10"><rect x="0.5" y="0.5" width="11" height="9" fill="none" stroke="#fff"/><path d="M0.5 0.5 6 5.5 11.5 0.5" fill="none" stroke="#fff"/></svg></span>dana@QuarvinStores.net</li>
    <li><span class="contact-icon"><svg width="12" height="12" viewBox="0 0 12 12"><circle cx="6" cy="6" r="5" fill="none" stroke="#fff"/><ellipse cx="6" cy="6" rx="2" ry="5" fill="none" stroke="#fff"/><line x1="1" y1="6" x2="11" y2="6" stroke="#fff"/></svg></span>www.quarvinstores.net</li>
  </ul>

  <div class="address">
    <svg width="12" height="16" viewBox="0 0 12 16"><path d="M6 0a6 6 0 0 1 6 6c0 4-6 10-6 10S0 10 0 6a6 6 0 0 1 6-6z" fill="#fff"/><circle cx="6" cy="6" r="2.2" fill="var(--gold)"/></svg>
    4120 Commerce Way Dr.<br>Harbor Point, FL 30218
  </div>
</section>

</body>
</html>
```